Original catchy book cover

I need a book cover for my book "The Copper Kettle Handbook" (https://quillpress.example/copperkettle). This will be a book self published on marketvale.
The book talks about the following concepts:
- Iterative product delivery
- Early discovery using feedback from customers
- Start small, think big, move fast
- Slice the product into valuable increments that can be validated with customers
- Experimental approach to deciding the next slice of work
A simple cover that stands out from the business books already out there! Some examples are:
https://www.marketvale.example/Tide-Harbor-Steady-Teams-Quietly-ebook/dp/X00AAA1111/ref=sr_1_1?ie=UTF8&qid=1000000001&sr=8-1&keywords=tide+and+harbor
https://www.marketvale.example/Copper-Kettle-Almanac-Brew-Ideas-ebook/dp/X00BBB2222/ref=sr_1_1?s=digital-text&ie=UTF8&qid=1000000002&sr=1-1&keywords=copper+kettle+almanac
https://www.marketvale.example/Orchard-Paths-Rewoven-Compass-Fogbanks-ebook/dp/X00CCC3333/ref=pd_sim_351_2?_encoding=UTF8&psc=1&refRID=ZZZZZZZZZZZZZZZZZZZZ
Lastly, attached are 2 draft covers that i've been playing with. Would love a graphic as part of the cover if it makes sense in your design! The graphic should tie to the meaning or themes of the book. Emphasis on ways of working, collaboration, experimentation, hypothesis, agile, incremental or adaptive. Those are some words that describe the content of the book.
Alternatively, something abstract could also be an option if a literal graphic doesn't suit the theme of your design.
Target Market(s)
Product owners, scrum masters, people in the agile community, software developers, designers
Industry/Entity Type
Information Technology
Font styles to use
Colors
Designer to choose colors to be used in the design.
Requirements
Must have
- Title, Subtitle, Author Name
- Back of the book should have space for a description (use lorem ipsum for now)
- Please use the editorial logo
- (please omit "created by Tomas Verhelst" because the editorial logo replaces that.
- The design must be original art or graphics (i.e. it should be similar to another cover in this topic).
Nice to have
- A graphic would be ideal if it is relevant to the book topic, otherwise a nice simple cover that uses colors or patterns that are easy to recall.
- The color suggestions below are suggestions only. Do not feel you have to incorporate all the colors and feel free to recommend an alternate palette.
Should not have
- Clipart or generic stock art photos. Images for the sake of images, traditional logos (e.g. a computer, a phone etc unless it's part of an overall theme that ties the logos together).

```html
<!DOCTYPE html>
<html lang="en">
<head>
<meta charset="utf-8">
<title>The Copper Kettle Handbook — Cover</title>
<link rel="stylesheet" href="https://fonts.googleapis.com/css2?family=Montserrat:wght@500;700;800;900&display=swap">
<style>
  :root {
    --cover-cream: #F3E6CF;
    --title-copper: #B5562A;
    --title-teal: #1E6D68;
    --title-navy: #1D2A45;
    --step-light: #E39B62;
    --ink: #1A1A1A;
  }
  * { margin: 0; padding: 0; box-sizing: border-box; }
  html, body {
    width: 848px;
    height: 1200px;
    overflow: hidden;
    background: var(--cover-cream);
  }
  .cover {
    position: relative;
    width: 848px;
    height: 1200px;
    background: var(--cover-cream);
    font-family: "Montserrat", Arial, sans-serif;
    color: var(--ink);
  }
  .title-block {
    position: absolute;
    inset: 0;
    width: 848px;
    height: 1200px;
  }
  .title-word {
    font-family: "Montserrat", Arial, sans-serif;
    font-weight: 800;
  }
  .title-article {
    font-family: "Montserrat", Arial, sans-serif;
    font-weight: 700;
    letter-spacing: 10px;
    fill: var(--title-navy);
  }
  .title-word--copper { fill: var(--title-copper); }
  .title-word--teal { fill: var(--title-teal); }
  .title-word--navy { fill: var(--title-navy); }
  .increment-step { fill: var(--title-copper); }
  .increment-step--light { fill: var(--step-light); }
  .title-rule { fill: var(--title-navy); }
  .subtitle {
    position: absolute;
    top: 768px;
    left: 0;
    width: 848px;
    text-align: center;
    font-size: 21px;
    font-weight: 500;
    line-height: 30px;
    letter-spacing: 0.2px;
  }
  .author {
    position: absolute;
    top: 972px;
    left: 0;
    width: 848px;
    text-align: center;
    font-size: 50px;
    font-weight: 900;
    letter-spacing: 1px;
    line-height: 60px;
  }
</style>
</head>
<body>
<main class="cover">
  <svg class="title-block" viewBox="0 0 848 1200" xmlns="http://www.w3.org/2000/svg" aria-labelledby="book-title">
    <title id="book-title">The Copper Kettle Handbook</title>
    <rect class="title-rule" x="214" y="160" width="60" height="6"/>
    <text class="title-article" font-size="34" x="290" y="176">THE</text>
    <text class="title-word title-word--copper" font-size="154" x="212" y="311" textLength="468" lengthAdjust="spacingAndGlyphs">COPPER</text>
    <text class="title-word title-word--teal" font-size="154" x="212" y="449" textLength="468" lengthAdjust="spacingAndGlyphs">KETTLE</text>
    <text class="title-word title-word--teal" font-size="157" x="212" y="577" textLength="342" lengthAdjust="spacingAndGlyphs">HAND</text>
    <g class="increments">
      <rect class="increment-step increment-step--light" x="584" y="550" width="18" height="27"/>
      <rect class="increment-step increment-step--light" x="608" y="523" width="18" height="54"/>
      <rect class="increment-step" x="632" y="496" width="18" height="81"/>
      <rect class="increment-step" x="656" y="469" width="18" height="108"/>
    </g>
    <text class="title-word title-word--navy" font-size="154" x="212" y="708" textLength="468" lengthAdjust="spacingAndGlyphs">BOOK</text>
  </svg>

  <p class="subtitle">a working handbook for shipping small slices<br>and growing products people value</p>
  <p class="author">MIRA THANH</p>
</main>
</body>
</html>
```